Geschäftspapiere für Rechtsanwaltskanzlei
Zielgruppe
Rechtsanwaltskanzlei mit dem Spezialgebiet Urheber-/Medienrecht; Mandanten sind Urheber, insbesondere von Musik- und Filmwerken, sowie Unternehmen, deren Unternehmenszweck die Herstellung- und Verwertung vorstehender Werke ist (z.B. Verlage, Filmproduktionsunternehmen). Das Design soll seriös sein, dabei aber einen modernen Touch haben.
Aufgabenstellung
Das Design muss im schwarz-weiß Ausdruck gut lesbar sein.
Es sollen folgende Informationen enthalten sein
Rechtsanwaltskanzlei Brunsmann
Rechtsanwältin Helga Brunsmann, MBA
Wiesenhang 27
14059 Berlin
Helga.Brunsmann@ra-brunsmann.com
Tel: +491524718260

```html
<!DOCTYPE html>
<html lang="de">
<head>
<meta charset="utf-8">
<title>Briefbogen – Rechtsanwaltskanzlei Brunsmann</title>
<link rel="stylesheet" href="https://fonts.googleapis.com/css2?family=Inter:wght@200;300;400&display=swap">
<style>
  :root {
    --paper: #ffffff;
    --ink: #1a1a1a;
    --ink-soft: #3a3a3a;
    --band: #67686a;
    --frame: #7a7a7a;
    --accent: #776a5e;
  }
  html, body {
    margin: 0;
    padding: 0;
    width: 863px;
    height: 1200px;
    overflow: hidden;
    background: var(--paper);
  }
  .sheet {
    position: relative;
    width: 863px;
    height: 1200px;
    font-family: "Inter", Arial, sans-serif;
    color: var(--ink);
  }
  .frame {
    position: absolute;
    left: 38px; top: 43px;
    width: 786px; height: 1113px;
    border: 1px solid var(--frame);
    box-sizing: border-box;
  }
  .side-band {
    position: absolute;
    left: 38px; top: 43px;
    width: 18px; height: 1114px;
    background: var(--band);
  }
  .fold-mark {
    position: absolute;
    left: 38px;
    width: 18px; height: 1px;
    background: var(--paper);
  }
  .fold-mark--upper { top: 436px; }
  .fold-mark--lower { top: 599px; }

  .accent-bar {
    position: absolute;
    left: 816px;
    width: 9px;
    background: var(--accent);
  }
  .accent-bar--contact { top: 253px; height: 121px; }
  .accent-bar--bank { top: 1050px; height: 107px; }

  .brand {
    position: absolute;
    right: 65px; top: 100px;
    text-align: right;
  }
  .brand__name {
    display: block;
    font-weight: 200;
    font-size: 54px;
    line-height: 1;
    letter-spacing: -1px;
    color: var(--ink);
  }
  .brand__tagline {
    display: block;
    margin-top: 7px;
    font-weight: 300;
    font-size: 16.5px;
    letter-spacing: 2.9px;
    margin-right: -2.9px;
    color: var(--ink);
  }

  .return-address {
    position: absolute;
    left: 120px; top: 219px;
    width: 300px;
    border-bottom: 1px solid var(--ink-soft);
    padding: 0 0 4px 20px;
    box-sizing: border-box;
    font-size: 9.3px;
    font-weight: 300;
    color: var(--ink-soft);
    white-space: nowrap;
  }

  .contact, .bank {
    position: absolute;
    right: 65px;
    text-align: right;
    font-weight: 300;
    color: var(--ink-soft);
    font-size: 10.5px;
    line-height: 1.1;
  }
  .contact { top: 254px; }
  .contact p, .bank p { margin: 0; }
  .contact__name {
    font-size: 13px;
    font-weight: 400;
    color: var(--ink);
  }
  .contact__title { margin-top: 3px !important; }
  .contact__address { margin-top: 11px !important; line-height: 1.4; }
  .contact__phone { margin-top: 8px !important; }
  .contact__mail { margin-top: 9px !important; }

  .fold-dot {
    position: absolute;
    top: 388px;
    width: 1px; height: 1px;
    background: var(--ink-soft);
  }
  .fold-dot--left { left: 112px; }
  .fold-dot--right { left: 431px; }

  .bank { top: 1063px; font-size: 10px; }
  .bank__block { margin-top: 7px !important; }
</style>
</head>
<body>
  <div class="sheet">
    <div class="frame"></div>
    <div class="side-band"></div>
    <div class="fold-mark fold-mark--upper"></div>
    <div class="fold-mark fold-mark--lower"></div>

    <div class="brand">
      <span class="brand__name">BRUNSMANN</span>
      <span class="brand__tagline">Rechtsanwaltskanzlei</span>
    </div>

    <div class="return-address">BRUNSMANN Rechtsanwaltskanzlei · Wiesenhang 27 · 14059 Berlin</div>

    <div class="accent-bar accent-bar--contact"></div>
    <div class="contact">
      <p class="contact__name">Helga Brunsmann</p>
      <p class="contact__title">Rechtsanwältin, MBA</p>
      <p class="contact__address">Wiesenhang 27<br>14059 Berlin</p>
      <p class="contact__phone">Tel.&nbsp; +49 152 471 82 60</p>
      <p class="contact__mail">Helga.Brunsmann@ra-brunsmann.com</p>
    </div>

    <span class="fold-dot fold-dot--left"></span>
    <span class="fold-dot fold-dot--right"></span>

    <div class="accent-bar accent-bar--bank"></div>
    <div class="bank">
      <p>Spreebank Berlin</p>
      <p class="bank__block">BIC:<br>ABCDEFGH987</p>
      <p class="bank__block">IBAN:<br>DE88 8888 0000 8888 0000 88</p>
    </div>
  </div>
</body>
</html>
```